8 New Banner Campaigns

Task Description
I want banners created for 8 campaigns.

For each campaign I need these 6 banner sizes created:

Web Banner Sizes (300x250, 468x60, 160x600)
One of each of these sizes, so 3 web banners

Mobile Banner Sizes (300x50, 216x36, 240x240)

campaign 1
http://brivapagehost.com/_PROJECT_/fundmarket/index.php
Done right
$10,000 Money-back guarantee!

Call Now For Your Top Local Electrician!

campaign2
http://www.palmcrestretreat.com

a weight loss journey that can change your life

campaign 3
http://www.norvexlistings.com/m/delta-in-financial-planner/

Professional financial planning
Tax planning
Estate planning
Retirement planning
Wealth Management

Call Now for Details!

campaign4
www.areatradeappraisals.com/Farmington-CT/KIVO-Insurance-Agency-81342.html

Business insurance free quotes

campaign5
Summit debtrelief
http://www.norvexlistings.com/m/dayton-oh-bankruptcy-attorney/

Call Now for a No Cost Evaluation by a participating Summit Debtrelief Attorney.

campaign 6
http://brivapagehost.com/_PROJECT_/harbors/index.php

Is a reverse mortgage right for you?

Cash to live on while you stay in your home

Our caring experts will explain your options-Call Now

In tiny text at bottom:
No reverse mortgages in MD, IL, RI, and NC

campaign 7
http://www.freewheel-legal.com/

Dransfeld Law DUI defense

Campaign 8
http://www.craftacademies.edu/

The Craft Academies

Need these done ASAP..more to come!

Industry/Entity Type

Financial

Requirements
Must have
• Phone Number call to action on all banners.

```html
<!DOCTYPE html>
<html lang="en">
<head>
<meta charset="utf-8">
<title>Trade Sure! Electrician Banners</title>
<link rel="stylesheet" href="https://fonts.googleapis.com/css2?family=Arimo:ital,wght@0,700;1,700&family=Pathway+Gothic+One&display=swap">
<style>
  :root {
    --canvas: #ffffff;
    --maroon-light: #8e2c2c;
    --maroon-mid: #6a1c1c;
    --maroon-dark: #3d0d0d;
    --frame: #3a0a0a;
    --brand: #8a1c2b;
    --phone-blue: #1b2eff;
    --white: #ffffff;
    --ink: #000000;
    --photo-light: #e9e2d6;
    --photo-warm: #c7a98e;
    --photo-dark: #7a5a45;
    --icon-blue: #2f7fd1;
  }
  * { margin: 0; padding: 0; box-sizing: border-box; }
  html, body { width: 1200px; height: 1115px; overflow: hidden; background: var(--canvas); }
  body { position: relative; font-family: "Arimo", Arial, sans-serif; }

  .banner {
    position: absolute;
    overflow: hidden;
    border: 2px solid var(--frame);
    background: radial-gradient(ellipse at 30% 30%, var(--maroon-light), var(--maroon-mid) 55%, var(--maroon-dark));
  }
  .banner svg.backdrop { position: absolute; inset: 0; width: 100%; height: 100%; }
  .banner > * { position: absolute; }

  .skyscraper { left: 6px; top: 6px; width: 295px; height: 1105px; }
  .leaderboard { left: 330px; top: 6px; width: 866px; height: 110px; }
  .rectangle { left: 330px; top: 175px; width: 557px; height: 461px; }

  .brand { display: flex; align-items: center; gap: 6px; color: var(--brand); font-weight: 700; white-space: nowrap; }
  .brand-dot { border-radius: 50%; background: var(--brand); flex: none; }

  .guarantee { color: var(--white); font-style: italic; font-weight: 700; text-align: center; }
  .headline {
    font-family: "Pathway Gothic One", "Arial Narrow", sans-serif;
    color: var(--white);
    text-align: center;
    white-space: nowrap;
    transform: scaleY(1.5);
    text-shadow:
      2px 0 0 var(--ink), -2px 0 0 var(--ink), 0 2px 0 var(--ink), 0 -2px 0 var(--ink),
      2px 2px 0 var(--ink), -2px 2px 0 var(--ink), 2px -2px 0 var(--ink), -2px -2px 0 var(--ink),
      3px 3px 3px rgba(0,0,0,.6);
  }
  .call-now { color: var(--white); font-style: italic; font-weight: 700; white-space: nowrap; }
  .phone-box {
    background: var(--white);
    border-radius: 14px;
    display: flex; align-items: center; justify-content: center; gap: 8px;
  }
  .phone-number {
    display: inline-block;
    font-family: "Pathway Gothic One", "Arial Narrow", sans-serif;
    color: var(--phone-blue);
    white-space: nowrap;
    line-height: 1;
    transform: scaleY(1.3);
  }
  .call-pill {
    background: var(--white); border-radius: 999px;
    color: var(--ink); font-style: italic; font-weight: 700;
    display: flex; align-items: center; justify-content: center;
  }
  .phone-icon { border-radius: 50%; flex: none; }
</style>
</head>
<body>

<!-- 160 x 600 -->
<section class="banner skyscraper">
  <svg class="backdrop" viewBox="0 0 291 1101" preserveAspectRatio="none">
    <defs>
      <linearGradient id="photoTall" x1="0" y1="0" x2="1" y2="1">
        <stop offset="0" stop-color="var(--photo-light)"/>
        <stop offset=".6" stop-color="var(--photo-warm)"/>
        <stop offset="1" stop-color="var(--photo-dark)"/>
      </linearGradient>
    </defs>
    <path d="M0 0H291V312C200 322 80 300 0 246Z" fill="var(--white)"/>
    <g role="img" aria-label="Smiling customer service agent wearing a headset">
      <path d="M60 0H291V298C210 306 120 292 60 262Z" fill="url(#photoTall)"/>
    </g>
  </svg>
  <div class="brand" style="left:10px; top:12px; font-size:25px;">
    <span class="brand-dot" style="width:30px; height:30px;"></span>Trade Sure!
  </div>
  <p class="guarantee" style="left:0; width:291px; top:363px; font-size:35px; line-height:44px;">$10,000<br>Money-back<br>guarantee!</p>
  <p class="headline" style="left:0; width:291px; top:604px; font-size:66px; line-height:77px;">For<br>Your Top Local<br>Electrician!</p>
  <p class="call-now" style="left:0; width:291px; top:932px; font-size:36px; text-align:center;">Call Now</p>
  <div class="phone-box" style="left:30px; top:1008px; width:232px; height:72px;">
    <span class="phone-number" style="font-size:47px;">555-555-5555</span>
  </div>
</section>

<!-- 468 x 60 -->
<section class="banner leaderboard">
  <svg class="backdrop" viewBox="0 0 862 106" preserveAspectRatio="none">
    <defs>
      <linearGradient id="photoWide" x1="0" y1="0" x2="1" y2="1">
        <stop offset="0" stop-color="var(--photo-light)"/>
        <stop offset=".6" stop-color="var(--photo-warm)"/>
        <stop offset="1" stop-color="var(--photo-dark)"/>
      </linearGradient>
    </defs>
    <path d="M515 0H862V106H510C490 70 500 30 515 0Z" fill="var(--white)"/>
    <g role="img" aria-label="Smiling customer service agent wearing a headset">
      <rect x="712" y="0" width="150" height="106" fill="url(#photoWide)"/>
    </g>
  </svg>
  <p class="guarantee" style="left:14px; top:6px; font-size:27px; line-height:30px; white-space:nowrap;">$10,000 Money-back guarantee!</p>
  <p class="headline" style="left:14px; top:59px; font-size:37px; line-height:44px;">For Your Top Local Electrician!</p>
  <div class="call-pill" style="left:389px; top:64px; width:112px; height:32px; font-size:19px;">Call Now</div>
  <div class="brand" style="left:532px; top:10px; font-size:23px;">
    <span class="brand-dot" style="width:28px; height:28px;"></span>Trade Sure!
  </div>
  <div class="phone-box" style="left:548px; top:60px; width:156px; height:42px; border-radius:10px;">
    <span class="phone-number" style="font-size:35px;">555-555-5555</span>
  </div>
</section>

<!-- 300 x 250 -->
<section class="banner rectangle">
  <svg class="backdrop" viewBox="0 0 553 457" preserveAspectRatio="none">
    <defs>
      <linearGradient id="photoRect" x1="0" y1="0" x2="1" y2="1">
        <stop offset="0" stop-color="var(--photo-light)"/>
        <stop offset=".6" stop-color="var(--photo-warm)"/>
        <stop offset="1" stop-color="var(--photo-dark)"/>
      </linearGradient>
    </defs>
    <path d="M250 0H553V322C430 300 320 230 270 120C255 80 250 40 250 0Z" fill="var(--white)"/>
    <g role="img" aria-label="Smiling customer service agent wearing a headset">
      <path d="M290 78H553V308C450 286 360 230 310 150C298 128 292 104 290 78Z" fill="url(#photoRect)"/>
    </g>
  </svg>
  <p class="call-now" style="left:22px; top:24px; font-size:44px;">Call Now</p>
  <div class="phone-box" style="left:9px; top:124px; width:245px; height:66px; justify-content:flex-start; padding-left:12px;">
    <svg class="phone-icon" width="46" height="46" viewBox="0 0 46 46" aria-hidden="true">
      <circle cx="23" cy="23" r="22" fill="var(--icon-blue)"/>
      <circle cx="23" cy="23" r="15" fill="none" stroke="var(--white)" stroke-width="3"/>
      <path d="M17 15c2 0 3 3 3 4s-2 2-1 4 2 3 4 4 2-1 3-1 4 1 4 3-2 3-4 2-6-2-8-5-3-6-2-9 1-2 1-2z" fill="var(--white)"/>
    </svg>
    <span class="phone-number" style="font-size:39px;">555-555-5555</span>
  </div>
  <div class="brand" style="left:288px; top:20px; font-size:30px;">
    <span class="brand-dot" style="width:40px; height:40px;"></span>Trade Sure!
  </div>
  <p class="headline" style="left:0; width:553px; top:278px; font-size:58px; line-height:60px;">For Your Top Local Electrician!</p>
  <p class="guarantee" style="left:0; width:553px; top:396px; font-size:33px; line-height:38px; white-space:nowrap;">$10,000 Money-back guarantee!</p>
</section>

</body>
</html>
```